Redesign trade show stand graphics for Harbourline Panels

Update existing graphics of a trade show stand consisting of 2 walls. See the current design attached.

Left wall size is 2.4m high x 2700mm wide (made up of 3 pieces of 2400mm high x 900mm wide). The artwork will be printed on self adhesive stickers to cover the 2 walls.

NEW DESIGN LEFT WALL (2.4m high x 3m wide)
Headline at the top of the wall should read:
RENOVATE YOUR KITCHEN
the quick, easy and cost effective way:
JUST REPLACE THE DOORS and panels
• Cost effective: Save $$$
• Quick: approx. 15 working days
• Easy: No mess or inconvenience
• Polyurethane finish, unlimited choice of colours
• Measure, quote and install - DIY or contact our installers
• Delivery Australia wide
Harbourline Panels logo at top of left and right walls. See logo attached. “Australian made” logo somewhere on the wall (logo attached)
The main body of the left wall will contain a “before” and “after” photo of a kitchen. Size of “before” shot approximately 250mm wide x 150mm high and “after” shot approximately 1m wide x 600mm high. Photo with higher resolution will be supplied.
Text:
• We replace doors, panels, drawer fronts and kickboards - all painted in polyurethane.
• We drill doors for new or existing hinges. We supply Vorn soft closing hinges, door handles, wardrobe door tracks and decorative items such as corbels, flutes and rosettes and capping.
• Our installers measure, quote and install or save money and do it yourself - DIY
Headline under the above: UPDATE YOUR BUILT IN WARDROBES WITH NEW DOORS
Sub headline: Custom made to your sizes and painted in polyurethane in the colour of your choice
2 photos of wardrobes to go under this headline

NEW DESIGN RIGHT WALL (2.4m high x 2800mm wide made up of 1 x 1000mm piece and 2 x 900mm pieces)
Visit our website: harbourlinepanels.com.au
Headline: SAVE TIME AND MONEY – REPLACE YOUR OLD DOORS (and panels)
Sub headline: WITH ONES PAINTED IN POLYURETHANE
Sub sub headline:
TO GET A QUOTE:
• DIY measure doors and panels and fill in our Quote Form or
• Contact our installers to measure, quote and install

At 1.5m high: 2 rows of 7 rectangular outlines 400mm high x 300mm wide (for sample doors that will be hung on the wall).
Directly under that, another headline:
Many more designs in our showroom at
47 Kestrel Avenue, Marlow Heights NSW 2837
Phone: (02) 9318 6072
Email: sales@harbourlinepanels.com.au
Website: harbourlinepanels.com.au
Place image of our showroom (attached) to the left or right.

“Australian made” logo and "Trade and public welcome" logo somewhere on the wall (logos attached).
Small listing of approximately A5 size of “What we do”, “What we don’t do” and “What you do”. These will be supplied in bullet points.
Another image to use is uploaded below.

Target Market(s)

Home owners, home renovators

Industry/Entity Type

Trade

Font styles to use
Sans Serif
Other font styles liked:
• A font similar to that used on our website www.harbourlinepanels.com.au

Colors
f8972e

Requirements
Must have
• The background colour of the stand artwork should remain the same bright colour of our logo. The fonts should be similar to that used on our website www.harbourlinepanels.com.au
Nice to have
• Fun and engaging design

```html
<!DOCTYPE html>
<html lang="en">
<head>
<meta charset="utf-8">
<title>Harbourline Panels – Left Wall</title>
<link rel="stylesheet" href="https://fonts.googleapis.com/css2?family=Roboto+Condensed:ital,wght@0,400;0,700;1,700&family=Questrial&display=swap">
<style>
  :root {
    --orange: #f8972e;
    --ink: #111111;
    --text: #1d1d1d;
    --paper: #f1f1f1;
    --paper-shade: #e4e4e4;
    --dark: #2b2b2b;
    --white: #ffffff;
  }
  * { margin: 0; padding: 0; box-sizing: border-box; }
  html, body { width: 1200px; height: 959px; overflow: hidden; }
  body { font-family: "Questrial", sans-serif; color: var(--text); }

  .wall {
    position: relative; width: 1200px; height: 959px; overflow: hidden;
    background: linear-gradient(135deg, var(--paper) 0%, var(--white) 45%, var(--paper-shade) 100%);
  }

  .headline-band {
    position: absolute; left: 0; top: 26px; width: 588px; height: 48px;
    background: var(--orange);
    clip-path: polygon(0 0, 97.5% 0, 100% 50%, 97.5% 100%, 0 100%);
  }
  .headline {
    position: absolute; left: 48px; top: 25px;
    font-family: "Roboto Condensed", sans-serif; font-weight: 700;
    font-size: 46px; line-height: 50px; color: var(--ink); letter-spacing: -0.8px;
  }
  .subline { position: absolute; left: 53px; top: 84px; font-size: 25px; line-height: 32px; white-space: nowrap; }
  .subline em {
    font-family: "Roboto Condensed", sans-serif; font-weight: 700; font-style: italic;
    color: var(--orange); font-size: 27px; margin-left: 4px;
  }

  .benefit { position: absolute; top: 158px; width: 219px; text-align: center; }
  .benefit-tag {
    height: 36px; background: var(--orange); color: var(--white);
    font-family: "Roboto Condensed", sans-serif; font-size: 31px; line-height: 36px;
    clip-path: polygon(4% 0, 96% 0, 100% 50%, 96% 100%, 4% 100%, 0 50%);
  }
  .benefit-text {
    margin: 14px -80px 0; font-size: 24px; line-height: 32px; letter-spacing: 0.8px; white-space: nowrap;
  }
  .benefit-text strong {
    font-family: "Roboto Condensed", sans-serif; font-weight: 700; font-size: 41px;
    letter-spacing: 0; vertical-align: -5px; margin-left: 8px;
  }
  .benefit--cost { left: 60px; }
  .benefit--quick { left: 387px; }
  .benefit--easy { left: 716px; }

  .rule { position: absolute; left: 0; top: 256px; width: 1001px; height: 2px; background: var(--ink); }

  .brand { position: absolute; left: 1028px; top: 40px; width: 160px; }
  .brand-mark { width: 30px; height: 30px; background: var(--orange); margin-bottom: 12px; }
  .brand-name {
    font-family: "Roboto Condensed", sans-serif; font-weight: 700; font-size: 31px;
    line-height: 34px; color: var(--ink);
  }

  .feature-icon { position: absolute; width: 90px; height: 90px; }
  .feature-icon--finish { left: 243px; top: 277px; }
  .feature-icon--measure { left: 589px; top: 277px; }
  .feature-icon--delivery { left: 874px; top: 274px; }
  .feature { position: absolute; font-size: 24.5px; line-height: 30px; letter-spacing: 0.3px; white-space: nowrap; }
  .feature--finish { left: 138px; top: 379px; }
  .feature--measure { left: 471px; top: 378px; width: 320px; text-align: center; line-height: 31px; }
  .feature--delivery { left: 807px; top: 373px; width: 220px; text-align: center; line-height: 33px; }

  .photo-label { position: absolute; font-style: italic; font-size: 17px; line-height: 20px; }
  .photo-label--before { left: 69px; top: 432px; }
  .photo-label--after { left: 369px; top: 499px; }
  .photo { position: absolute; }
  .photo--before { left: 26px; top: 454px; width: 99px; height: 58px; background: linear-gradient(135deg, #7a3d1c, #a4602f 55%, #d9cbb7); }
  .photo--after { left: 21px; top: 523px; width: 400px; height: 238px; background: linear-gradient(180deg, #e8e3d9 0%, #d8d1c2 55%, #c9bfae 100%); }
  .after-badge {
    position: absolute; left: 26px; top: 712px; width: 68px; height: 48px; border-radius: 50%;
    background: var(--white); font-family: "Roboto Condensed", sans-serif; font-weight: 700;
    font-size: 16px; line-height: 48px; text-align: center; color: var(--ink);
  }

  .points {
    position: absolute; left: 433px; top: 471px; width: 760px; list-style: none;
    font-size: 18.5px; line-height: 24.5px; letter-spacing: 0.3px; white-space: nowrap;
  }
  .points li { position: relative; padding-left: 14px; margin-bottom: 17px; }
  .points li::before { content: "•"; position: absolute; left: 0; }

  .wardrobe-band {
    position: absolute; left: 495px; top: 658px; width: 581px; height: 36px; background: var(--orange);
    clip-path: polygon(2% 0, 98% 0, 100% 50%, 98% 100%, 2% 100%, 0 50%);
    font-family: "Roboto Condensed", sans-serif; font-weight: 700; font-style: italic;
    font-size: 24px; line-height: 36px; text-align: center; color: var(--ink);
  }
  .wardrobe-note {
    position: absolute; left: 433px; top: 712px; font-size: 18.5px; line-height: 24px;
    letter-spacing: 0.3px; white-space: nowrap;
  }
  .wardrobe-note::before { content: "•"; margin-right: 6px; }

  .gallery { position: absolute; left: 0; top: 773px; width: 950px; height: 186px; background: var(--orange); }
  .gallery-photo { position: absolute; top: 7px; height: 179px; }
  .gallery-photo--showroom { left: 0; width: 467px; background: linear-gradient(90deg, #e9e3d4 0%, #f2efe7 45%, #c9ced4 100%); }
  .gallery-photo--bedroom { left: 476px; width: 465px; background: linear-gradient(90deg, #f6f6f6 0%, #ececec 60%, #cfd0da 100%); }

  .made-panel { position: absolute; left: 950px; top: 849px; width: 250px; height: 110px; background: var(--dark); }
  .made-badge { position: absolute; left: 150px; top: 14px; width: 66px; height: 58px; border-radius: 10px; background: var(--orange); }
</style>
</head>
<body>
<main class="wall">
  <div class="headline-band"></div>
  <h1 class="headline">RENOVATE YOUR KITCHEN</h1>
  <p class="subline">the quick, easy and cost effective way: <em>JUST REPLACE THE DOORS &nbsp;and panels</em></p>

  <div class="benefit benefit--cost"><div class="benefit-tag">Cost effective:</div><p class="benefit-text">Save <strong>$$$</strong></p></div>
  <div class="benefit benefit--quick"><div class="benefit-tag">Quick:</div><p class="benefit-text">approx.15 working days</p></div>
  <div class="benefit benefit--easy"><div class="benefit-tag">Easy:</div><p class="benefit-text">No mess or inconvenience</p></div>

  <div class="rule"></div>

  <div class="brand"><div class="brand-mark"></div><p class="brand-name">Harbourline<br>Panels</p></div>

  <svg class="feature-icon feature-icon--finish" viewBox="0 0 90 90" aria-hidden="true">
    <circle cx="45" cy="45" r="41" fill="#fff" stroke="#f8972e" stroke-width="5"/>
    <line x1="28" y1="28" x2="62" y2="62" stroke="#1d1d1d" stroke-width="6" stroke-linecap="round"/>
    <line x1="62" y1="28" x2="28" y2="62" stroke="#f8972e" stroke-width="6" stroke-linecap="round"/>
  </svg>
  <svg class="feature-icon feature-icon--measure" viewBox="0 0 90 90" aria-hidden="true">
    <circle cx="45" cy="45" r="41" fill="#fff" stroke="#f8972e" stroke-width="5"/>
    <rect x="30" y="30" width="32" height="28" fill="none" stroke="#f8972e" stroke-width="3" transform="rotate(-30 46 44)"/>
    <polyline points="30,36 46,48 62,36" fill="none" stroke="#f8972e" stroke-width="3" transform="rotate(-30 46 44)"/>
    <line x1="20" y1="30" x2="30" y2="30" stroke="#1d1d1d" stroke-width="3"/>
    <line x1="20" y1="60" x2="30" y2="60" stroke="#1d1d1d" stroke-width="3"/>
  </svg>
  <svg class="feature-icon feature-icon--delivery" viewBox="0 0 90 90" aria-hidden="true">
    <circle cx="45" cy="45" r="41" fill="#fff" stroke="#f8972e" stroke-width="5"/>
    <rect x="30" y="32" width="26" height="22" fill="#f8972e"/>
    <path d="M56 38 H65 L71 46 V54 H56 Z" fill="#f8972e"/>
    <circle cx="38" cy="56" r="5" fill="#fff" stroke="#1d1d1d" stroke-width="3"/>
    <circle cx="63" cy="56" r="5" fill="#fff" stroke="#1d1d1d" stroke-width="3"/>
    <line x1="16" y1="38" x2="27" y2="38" stroke="#1d1d1d" stroke-width="3"/>
    <line x1="19" y1="45" x2="27" y2="45" stroke="#1d1d1d" stroke-width="3"/>
  </svg>

  <p class="feature feature--finish">Polyurethane finish,<br>unlimited choice of colours</p>
  <p class="feature feature--measure">Measure, quote and install<br>DIY or contact our installers</p>
  <p class="feature feature--delivery">Delivery<br>Australia wide</p>

  <p class="photo-label photo-label--before">Before</p>
  <div class="photo photo--before" role="img" aria-label="Kitchen before renovation with timber cabinet doors"></div>
  <p class="photo-label photo-label--after">After</p>
  <div class="photo photo--after" role="img" aria-label="Renovated kitchen with new white painted cabinet doors"></div>
  <div class="after-badge">After</div>

  <ul class="points">
    <li>We replace doors, panels, drawer fronts and kickboards - all painted in polyurethane.</li>
    <li>We drill doors for new or existing hinges. We supply Vorn soft closing hinges, door<br>handles, wardrobe door tracks and decorative items such as corbels, flutes and<br>rosettes and capping.</li>
    <li>Our installers measure, quote and install or save money and do it yourself - DIY</li>
  </ul>

  <div class="wardrobe-band">UPDATE YOUR BUILT IN WARDROBES WITH NEW DOORS</div>
  <p class="wardrobe-note">Custom made to your sizes and painted in polyurethane in the colour of your choice</p>

  <div class="gallery">
    <div class="gallery-photo gallery-photo--showroom" role="img" aria-label="Showroom with rows of white sample wardrobe and cabinet doors"></div>
    <div class="gallery-photo gallery-photo--bedroom" role="img" aria-label="Bedroom with new white built-in wardrobe doors"></div>
  </div>

  <div class="made-panel"><div class="made-badge" role="img" aria-label="Certification badge"></div></div>
</main>
</body>
</html>
```